Business Card Design

We are a manufacturing and distribution company with most of our customer base being supermarkets. We have established brand guidelines that are attached.

```html
<!DOCTYPE html>
<html lang="en">
<head>
<meta charset="utf-8">
<title>Norvale Business Card</title>
<link href="https://fonts.googleapis.com/css2?family=Montserrat:wght@500;700&family=Roboto:wght@400&display=swap" rel="stylesheet">
<style>
  :root {
    --bg: #2b2b2d;
    --card-dark: #111113;
    --card-light: #ffffff;
    --ink: #2e2e30;
    --blue: #1f78c1;
    --red: #e0262f;
    --grey: #5a5a5c;
    --white: #ffffff;
  }
  * { margin: 0; padding: 0; box-sizing: border-box; }
  html, body { width: 1200px; height: 929px; overflow: hidden; }
  body { background: var(--bg); position: relative; font-family: "Roboto", sans-serif; }

  .card {
    position: absolute;
    width: 600px;
    height: 343px;
    border-radius: 18px;
    box-shadow: 0 14px 30px rgba(0,0,0,0.45);
  }
  .card--back {
    left: 110px; top: 80px;
    background: radial-gradient(ellipse at 55% 40%, #1e1e20 0%, var(--card-dark) 70%);
    display: flex; align-items: center; justify-content: center;
  }
  .card--front { left: 490px; top: 500px; background: var(--card-light); }

  .brand {
    display: flex; align-items: center; gap: 14px;
    font-family: "Montserrat", sans-serif; font-weight: 700;
    letter-spacing: 2px;
  }
  .brand__mark { width: 34px; height: 34px; background: var(--blue); }
  .brand__name { line-height: 1; }
  .card--back .brand__name { font-size: 56px; color: var(--white); }
  .card--back .brand__mark { width: 44px; height: 44px; }

  .card--front .brand { position: absolute; right: 40px; top: 44px; }
  .card--front .brand__name { font-size: 36px; color: var(--ink); }

  .divider {
    position: absolute; left: 262px; right: 40px; top: 178px;
    height: 1.5px; background: var(--red);
  }

  .person { position: absolute; left: 40px; top: 152px; }
  .person__name {
    font-family: "Montserrat", sans-serif; font-weight: 700;
    font-size: 19px; color: var(--blue); letter-spacing: 0.3px;
  }
  .person__title {
    font-family: "Montserrat", sans-serif; font-weight: 500;
    font-size: 15px; color: var(--red); margin-top: 2px;
  }

  .contacts { position: absolute; left: 40px; top: 228px; list-style: none; }
  .contacts li {
    display: flex; align-items: center; gap: 10px;
    font-size: 15px; color: var(--grey); height: 24px;
  }
  .contacts svg { width: 15px; height: 15px; fill: none; stroke: var(--blue); stroke-width: 1.8; }

  .office {
    position: absolute; right: 40px; top: 196px;
    text-align: right; font-size: 15px; color: var(--grey); line-height: 1.4;
  }
  .office__name { color: var(--blue); font-size: 16px; }
</style>
</head>
<body>

  <section class="card card--back">
    <div class="brand">
      <span class="brand__mark"></span>
      <span class="brand__name">NORVALE</span>
    </div>
  </section>

  <section class="card card--front">
    <div class="brand">
      <span class="brand__mark"></span>
      <span class="brand__name">NORVALE</span>
    </div>

    <div class="divider"></div>

    <div class="person">
      <p class="person__name">LUKAS M. BRENNER</p>
      <p class="person__title">Managing Director</p>
    </div>

    <ul class="contacts">
      <li>
        <svg viewBox="0 0 16 16"><path d="M3 2h3l1.5 3.5-2 1.3a8 8 0 0 0 3.7 3.7l1.3-2L14 10v3a1 1 0 0 1-1 1A11 11 0 0 1 2 3a1 1 0 0 1 1-1z"/></svg>
        +32 (0)15 48 290
      </li>
      <li>
        <svg viewBox="0 0 16 16"><rect x="1.5" y="3.5" width="13" height="9" rx="1"/><path d="M1.5 4l6.5 5 6.5-5"/></svg>
        hello@norvalefoods.com
      </li>
      <li>
        <svg viewBox="0 0 16 16"><circle cx="8" cy="8" r="6.5"/><path d="M1.5 8h13M8 1.5c2.2 2 2.2 11 0 13M8 1.5c-2.2 2-2.2 11 0 13"/></svg>
        www.norvalefoods.com
      </li>
    </ul>

    <address class="office" style="font-style:normal">
      <p class="office__name">Norvale DP</p>
      <p>4870 Rue Delorme Laval</p>
      <p>Quebec H7N 2K8</p>
    </address>
  </section>

</body>
</html>
```